Web Design needed for logo design project

I am needing an interactive website for TC. Tandem Care Management is a nationwide company that combines the front desk administrative operation within Professional offices (Dental, Chiropractic, Optometry). I am needing a website designed that will provide information for potential new clients that are interested in joining our company to provide to them administrative support. I need a design for the marketing material within the folder, I will add content later. I am looking for clean crisp professional. No dancing teeth, hearts, or EKG signals please. We need it to appeal to 27-40 years old professionals. The professions are equally divided at 50/50 female to male. I already have a logo, it will be attached.
Updates

Target Market(s)

We need it to appeal to 27-40 years old professionals. The professions are equally divided at 50/50 female to male. I already have a logo, it will be attached.

Industry/Entity Type

Marketing

Requirements
Must have
• Needs to be in Word Press. It must have scalability to various screen sizes (Monitor, Phone screen, IPad, etc). Must have a customer portal capability, so professionals can access their information through a portal on the website. Have the capability to run a practice calculator or view a video requiring that it captures the visitors information so I can contact them regarding their interest in the site. Needs to have links to social media.

```html
<!DOCTYPE html>
<html lang="en">
<head>
<meta charset="utf-8">
<title>Tandem Care Management</title>
<link href="https://fonts.googleapis.com/css2?family=Noto+Serif:wght@700&family=Open+Sans:wght@400;600&display=swap" rel="stylesheet">
<style>
:root{
  --navy:#1b4c8c;
  --sky:#3db8e6;
  --sky-dark:#2fa5d6;
  --text:#7a7a7a;
  --line:#e6e6e6;
  --footer:#2b2b2b;
  --white:#ffffff;
}
*{box-sizing:border-box;margin:0;padding:0}
html,body{width:810px;height:1200px;overflow:hidden;background:var(--white)}
body{position:relative;font-family:"Open Sans",sans-serif;color:var(--text);border-top:2px solid var(--sky)}
.abs{position:absolute}
.serif{font-family:"Noto Serif",serif;font-weight:700}

.brand{left:66px;top:22px;color:var(--navy);display:flex;align-items:center;gap:8px}
.brand-square{width:26px;height:26px;background:var(--navy)}
.brand-name{font-family:"Noto Serif",serif;font-weight:700;font-size:14px;line-height:1.15;letter-spacing:.5px}
.brand-name span{display:block;font-size:8px;letter-spacing:4px}

.nav{right:66px;top:24px;display:flex;font-size:8px;text-transform:uppercase}
.nav a{color:#666;text-decoration:none;padding:0 20px;line-height:29px}
.nav a.active{background:var(--sky);color:var(--white);padding:0 17px}
.nav a:last-child{padding-right:0}

.hero{left:0;top:78px;width:810px;height:299px;background:linear-gradient(90deg,#9aa3a8 0%,#e9d6c2 28%,#e6ebee 50%,#cfd6dc 75%,#9ea9b3 100%)}
.hero-title{left:397px;top:146px;font-size:19px;color:var(--navy)}
.hero-text{left:397px;top:176px;width:345px;font-size:9px;line-height:17.5px;color:#555}
.arrows{left:706px;top:307px;display:flex;gap:2px}
.arrows span{width:17px;height:17px;background:#d8d8d8;display:flex;align-items:center;justify-content:center}

.card{top:337px;width:173px;height:132px;background:linear-gradient(180deg,#43bde9,#35aee0);color:var(--white);padding:20px 18px;box-shadow:0 6px 6px -4px rgba(0,0,0,.25)}
.card-head{display:flex;align-items:center;gap:9px;font-family:"Noto Serif",serif;font-weight:700;font-size:13px}
.card p{font-size:8px;line-height:15px;margin-top:11px}

.welcome-title{left:0;width:810px;top:502px;text-align:center;font-size:13px;color:var(--navy)}
.welcome-text{left:80px;width:650px;top:527px;text-align:center;font-size:8.5px;line-height:15.3px}
.btn{background:var(--sky);color:var(--white);font-family:"Noto Serif",serif;font-weight:700;display:flex;align-items:center;justify-content:center}
.portal{left:327px;top:588px;width:156px;height:35px;font-size:11px}

.rule{left:66px;width:678px;height:1px;background:var(--line)}
.section-title{left:66px;font-size:13px;color:var(--navy)}

.video{left:67px;top:717px;width:246px;height:148px;border:2px solid #eee;background:linear-gradient(120deg,#c9b3a5 0%,#e8ecef 55%,#bfe3ea 100%)}
.video-bar{position:absolute;left:0;right:0;bottom:0;height:14px;background:#1b1b1b}
.video-bar i{position:absolute;left:0;top:0;width:24px;height:2px;background:#d22}
.calc-text{left:337px;top:712px;width:407px;font-size:8.5px;line-height:15.3px}
.calc-text p+p{margin-top:6px}
.readmore{left:337px;top:838px;width:86px;height:28px;font-size:10px}

.client{top:964px;width:115px;height:83px;border:1px solid var(--line);display:flex;align-items:center;justify-content:center;font-size:15px;font-weight:600;color:#333}

.footer{left:0;top:1091px;width:810px;height:109px;background:var(--footer);color:var(--white)}
.footer .brand{color:var(--white);top:22px}
.footer .brand-square{background:var(--white)}
.copyright{left:66px;top:77px;font-size:8px}
.footer-nav{right:66px;top:24px;font-size:8px;display:flex;gap:10px}
.social{right:66px;top:57px;display:flex;gap:5px}
.social span{width:18px;height:18px;border-radius:50%;background:var(--white)}
</style>
</head>
<body>

<header>
  <div class="abs brand"><div class="brand-square"></div><div class="brand-name">TANDEM CARE<span>MANAGEMENT</span></div></div>
  <nav class="abs nav">
    <a class="active">Home</a><a>About Us</a><a>Services</a><a>Our Video</a><a>Blog</a><a>Contact Us</a>
  </nav>
</header>

<section class="abs hero" role="img" aria-label="Photo of a smiling professional woman in a bright office with colleagues blurred behind"></section>
<h1 class="abs hero-title serif">TANDEM CARE MANAGEMENT</h1>
<p class="abs hero-text">Usu doctus consulatu voluptatibus an, iuvaret euripidis in vel. In solum mazim nihil quo, te sit brute dicant graeci. Mea ad invidunt constituam appellantur. Eos eu enim ancillae, eos an facete adversarium.</p>
<div class="abs arrows">
  <span><svg width="7" height="9"><path d="M5 1L2 4.5L5 8" stroke="#333" fill="none" stroke-width="1.3"/></svg></span>
  <span style="background:#f2f2f2"><svg width="7" height="9"><path d="M2 1L5 4.5L2 8" stroke="#333" fill="none" stroke-width="1.3"/></svg></span>
</div>

<article class="abs card" style="left:110px">
  <div class="card-head">
    <svg width="30" height="38" viewBox="0 0 30 38" fill="none" stroke="#fff" stroke-width="2"><rect x="2" y="5" width="26" height="31" rx="3"/><rect x="10" y="1" width="10" height="6" rx="1"/><path d="M9 18l4 4 8-8"/><path d="M7 29h16M7 32h16"/></svg>
    DENTAL
  </div>
  <p>Lorem ipsum dolor sit amet, ne fugit dignissim consetetur vis. Ei eam sint ubique. Causae lucilius eam.</p>
</article>
<article class="abs card" style="left:319px">
  <div class="card-head">
    <svg width="33" height="33" viewBox="0 0 33 33" fill="#fff"><rect x="12" y="1" width="9" height="31" rx="2"/><rect x="12" y="1" width="9" height="31" rx="2" transform="rotate(60 16.5 16.5)"/><rect x="12" y="1" width="9" height="31" rx="2" transform="rotate(-60 16.5 16.5)"/></svg>
    CHIROPRACTIC
  </div>
  <p>Lorem ipsum dolor sit amet, ne fugit dignissim consetetur vis. Ei eam sint ubique. Causae lucilius eam.</p>
</article>
<article class="abs card" style="left:526px">
  <div class="card-head">
    <svg width="32" height="30" viewBox="0 0 32 30" fill="none" stroke="#fff" stroke-width="2"><rect x="1" y="6" width="30" height="23" rx="3"/><path d="M11 6V2h10v4"/><path d="M16 11v13M9.5 17.5h13" stroke-width="4"/></svg>
    OPTOMETRY
  </div>
  <p>Lorem ipsum dolor sit amet, ne fugit dignissim consetetur vis. Ei eam sint ubique. Causae lucilius eam.</p>
</article>

<h2 class="abs welcome-title serif">WELCOME TO TANDEM CARE MANAGEMENT</h2>
<p class="abs welcome-text">Usu doctus consulatu voluptatibus an, iuvaret euripidis in vel. In solum mazim nihil quo, te sit brute dicant graeci. Mea ad invidunt constituam appellantur. Eos eu enim ancillae, eos an facete adversarium. Per an quis sonet aperiam, ea sed justo viris pericula. Usu doctus consulatu voluptatibus an, iuvaret euripidis in vel. In solum mazim nihil quo, te sit brute dicant graeci. Mea ad invidunt constituam appellantur. Eos eu enim ancillae, eos an facete adversarium.</p>
<a class="abs btn portal">CUSTOMER PORTAL</a>

<div class="abs rule" style="top:656px"></div>

<h2 class="abs section-title serif" style="top:683px">PRACTISE CALCULATOR</h2>
<div class="abs video" role="img" aria-label="Video still of a smiling woman in glasses holding a tablet">
  <svg class="abs" style="left:108px;top:46px" width="30" height="30" viewBox="0 0 30 30"><circle cx="15" cy="15" r="13" fill="none" stroke="#fff" stroke-width="2"/><path d="M12 9l8 6-8 6z" fill="#fff"/></svg>
  <div class="video-bar"><i></i></div>
</div>
<div class="abs calc-text">
  <p>Lorem ipsum dolor sit amet, ne fugit dignissim consetetur vis. Ei eam sint ubique. Causae lucilius eam ea, ius facer docendi reprehendunt cu, no nec malis inermis. Viderer delicatissimi mel no, quo nihil percipit partiendo ne, ei nec everti numquam vulputate. Ex vel soluta hendrerit, debet dissentiet et nec. Ius quot summo exerci in.</p>
  <p>Lorem ipsum dolor sit amet, ne fugit dignissim consetetur vis. Ei eam sint ubique. Causae lucilius eam ea, ius facer docendi reprehendunt cu, no nec malis inermis. Viderer delicatissimi mel no, quo nihil percipit partiendo ne, ei nec everti numquam vulputate. Ex vel soluta hendrerit.</p>
</div>
<a class="abs btn readmore">READ MORE</a>

<div class="abs rule" style="top:902px"></div>

<h2 class="abs section-title serif" style="top:930px">OUR CLIENTS</h2>
<div class="abs client" style="left:66px">Velmora</div>
<div class="abs client" style="left:208px">Corvane</div>
<div class="abs client" style="left:349px">Brightwell</div>
<div class="abs client" style="left:490px">Nortica</div>
<div class="abs client" style="left:630px">Aldessa</div>

<footer class="abs footer">
  <div class="abs brand"><div class="brand-square"></div><div class="brand-name">TANDEM CARE<span>MANAGEMENT</span></div></div>
  <nav class="abs footer-nav">
    <span>Home</span><span>/</span><span>About Us</span><span>/</span><span>Services</span><span>/</span><span>Our Video</span><span>/</span><span>Blog</span><span>/</span><span>Contact Us</span>
  </nav>
  <div class="abs social"><span></span><span></span><span></span><span></span><span></span></div>
  <p class="abs copyright">Copyright @ 2014 TandemCareManagement.All Rights Reserved.</p>
</footer>

</body>
</html>
```